Website for Dental Office - The Brightcrest Clinic

The brightcrest clinic is a dental office offering cosmetic dentistry, general dentistry, and multi-specialty dental care all under one roof in our state-of-the-art cosmetic dental center. We are particularly striving to provide services that fit the need of the young generation. Thus, we hope to have a modern, professional concise website that represents our spirit.

*Should be able to switch from English to Chinese

6 sections besides homepage:
Home, Meet us, Services,
Patient Info, Cases&Reviews, Blog, Contact

The Services sections should contain multiple subsections such as cleaning and prevention, cosmetic dentistry, implant dentistry, removable dentures, etc...
The Patient Info section is also intended to contain several subsections such as
New Patient offer, accepted Insurance, patient portal, helpful tips, etc...

Target Market(s)

young generation

Coding

Number of Pages Required

5+ page

Font styles to use
Sans Serif

Colors
0592cd
33a6d7
85cae6
00a990
33b8a4
86cfc6
cee9f5
cfeae6
3277b5

Requirements
Must have
• *Should be able to switch from English to Chinese
Nice to have
• http://www.thebrightcrestclinic-example.com/
• As a reference, the above link is the current website, but we would like to change the appearance and the content (our new logo's picture is attached)

```html
<!DOCTYPE html>
<html lang="en">
<head>
<meta charset="utf-8">
<title>The Brightcrest Clinic</title>
<link href="https://fonts.googleapis.com/css2?family=Jost:wght@400;500;600&family=Lato:wght@400;700&display=swap" rel="stylesheet">
<style>
:root{
  --blue:#0592cd;--blue2:#33a6d7;--blue3:#85cae6;--pale:#cee9f5;--navy:#3277b5;
  --ink:#1d1d1d;--grey:#6b6b6b;--line:#d9dde0;--ring:#dbe7f0;
}
*{box-sizing:border-box;margin:0;padding:0}
html,body{width:1200px;height:4351px;overflow:hidden}
body{position:relative;background:#fff;font-family:'Lato',sans-serif;color:var(--ink)}
.abs{position:absolute}
.ring{position:absolute;border-radius:50%;border:16px solid var(--ring)}
.h-title{font-family:'Jost',sans-serif;font-weight:500;color:var(--blue);font-size:38px;line-height:1.1}
.center{left:0;width:1200px;text-align:center}
.rule{position:absolute;height:2px;background:var(--blue2);width:105px}
.sub{font-size:11px;line-height:19px;color:var(--ink)}
.btn{position:absolute;height:42px;border:1.5px solid var(--blue);background:#fff;color:var(--blue);font-family:'Jost',sans-serif;font-weight:500;font-size:14px;display:flex;align-items:center;justify-content:center}
.btn::after{content:"";position:absolute;left:6px;top:6px;right:-7px;bottom:-7px;border:1.5px solid var(--blue);border-top:none;border-left:none}
.field{position:absolute;height:44px;border:1px solid var(--line);border-radius:2px;font-size:11px;color:#777;padding:0 14px;display:flex;align-items:center;background:#fff}
.header-logo{left:160px;top:26px;display:flex;align-items:center;gap:10px;font-family:'Jost',sans-serif;font-weight:500;font-size:16px;color:var(--blue)}
.logo-sq{width:30px;height:30px;background:var(--blue2);border-radius:4px}
.nav{left:419px;top:38px;display:flex;gap:22px;font-size:11.5px;color:#fff}
.lang{left:977px;top:34px;width:61px;height:24px;background:var(--blue);color:#fff;font-size:11px;font-weight:700;display:flex;align-items:center;justify-content:space-around;padding:0 6px}
.info-card{position:absolute;top:842px;width:203px;height:91px;background:#fff;box-shadow:0 2px 8px rgba(0,0,0,.12);text-align:center;padding-top:14px}
.info-card h4{font-family:'Jost',sans-serif;font-weight:500;font-size:13px;margin-bottom:5px}
.info-card p{font-size:10px;line-height:16px;color:var(--grey);padding:0 12px}
.arrow-dot{position:absolute;left:50%;bottom:-16px;margin-left:-16px;width:32px;height:32px;border-radius:50%;background:var(--blue);display:flex;align-items:center;justify-content:center}
.svc{position:absolute;width:204px;height:188px;background:#fff;box-shadow:0 2px 10px rgba(0,0,0,.12);padding:14px;overflow:hidden}
.svc::before{content:"";position:absolute;right:-22px;top:-40px;width:92px;height:92px;border-radius:50%;background:#e8eef3}
.svc h4{position:absolute;left:14px;top:90px;font-family:'Jost',sans-serif;font-weight:500;font-size:14px}
.svc p{position:absolute;left:14px;right:10px;top:112px;font-size:10px;line-height:19px;color:var(--grey)}
.svc svg{position:relative}
.svc.active{background:var(--navy)}
.svc.active::before{background:rgba(255,255,255,.18)}
.svc.active h4,.svc.active p{color:#fff}
.avatar{position:absolute;border-radius:50%;background:radial-gradient(circle at 50% 40%,#c9a892,#6d5448);border:3px solid #fff;box-shadow:0 2px 8px rgba(0,0,0,.25)}
.review{position:absolute;top:3157px;width:280px;height:155px;background:#fff;box-shadow:0 2px 10px rgba(0,0,0,.12);padding:20px 14px;font-size:10.5px;line-height:19px;color:var(--grey)}
.review-avatar{position:absolute;top:3338px;width:60px;height:60px;border-radius:50%;background:radial-gradient(circle at 50% 40%,#b99a86,#3c3f4a)}
.review-name{position:absolute;top:3362px;font-size:10.5px;color:var(--blue);font-weight:700}
.foot-h{position:absolute;top:4058px;font-weight:700;font-size:13.5px}
.foot-list{position:absolute;top:4110px;list-style:none;font-size:11px;color:#555;line-height:23.6px}
.foot-list li::before{content:"";display:inline-block;width:6px;height:6px;border:1.5px solid var(--blue2);border-radius:50%;margin-right:10px;vertical-align:middle}
.social{position:absolute;top:4217px;width:36px;height:36px;border-radius:50%;border:1.5px solid var(--blue)}
</style>
</head>
<body>

<!-- decorative rings -->
<div class="ring" style="left:-150px;top:-130px;width:250px;height:250px"></div>
<div class="ring" style="left:1098px;top:530px;width:210px;height:210px"></div>
<div class="ring" style="left:-150px;top:1090px;width:225px;height:225px"></div>
<div class="ring" style="left:1108px;top:1465px;width:230px;height:230px"></div>
<div class="ring" style="left:-110px;top:2060px;width:230px;height:230px"></div>
<div class="ring" style="left:-170px;top:3310px;width:230px;height:230px"></div>
<div class="ring" style="left:1112px;top:3630px;width:230px;height:230px"></div>
<div class="ring" style="left:-160px;top:4070px;width:220px;height:220px"></div>

<!-- hero -->
<svg class="abs" style="left:0;top:0" width="1200" height="380" role="img" aria-label="Photo of a dentist examining a patient's teeth">
  <defs><linearGradient id="heroG" x1="0" y1="0" x2="1" y2="1"><stop offset="0" stop-color="#9fd2ea"/><stop offset=".55" stop-color="#4aa9d6"/><stop offset="1" stop-color="#2b8fc4"/></linearGradient></defs>
  <path d="M305,0 C360,200 520,380 720,365 C900,350 1000,300 1200,362 L1200,0 Z" fill="url(#heroG)"/>
</svg>
<div class="abs header-logo"><span class="logo-sq"></span>The Brightcrest Clinic</div>
<nav class="abs nav"><span>Home</span><span>About Us</span><span>Services</span><span>Meet us</span><span>Patient Info</span><span>Cases&amp;Reviews</span><span>Blog</span><span>Contact</span></nav>
<div class="abs lang"><span>Eng</span><svg width="8" height="6"><path d="M0 0h8L4 6z" fill="#fff"/></svg></div>

<div class="rule" style="left:162px;top:176px"></div>
<h1 class="abs h-title" style="left:162px;top:182px;font-size:42px;line-height:52px">One Stop The<br>Brightcrest Clinic</h1>
<p class="abs sub" style="left:162px;top:294px;width:300px;font-size:12px;line-height:20px">Lorem Ipsum is simply dummy text of the printing and typesetting industry.</p>
<div class="btn" style="left:160px;top:355px;width:195px">Book An Appointment</div>
<div class="abs" style="left:682px;top:327px;width:56px;height:56px;border-radius:50%;background:#fff;box-shadow:0 2px 10px rgba(0,0,0,.2);display:flex;align-items:center;justify-content:center"><svg width="14" height="16"><path d="M2 1l11 7-11 7z" fill="var(--blue)"/></svg></div>

<!-- patient info -->
<div class="rule" style="left:547px;top:470px"></div>
<h2 class="abs h-title center" style="top:478px">Patient Info</h2>
<p class="abs sub center" style="top:527px">Prior to your first appointment, we request that you<br>please download and complete</p>
<div class="field" style="left:160px;top:593px;width:283px">Name:</div>
<div class="field" style="left:460px;top:593px;width:280px">Email</div>
<div class="field" style="left:757px;top:593px;width:281px">Phone:</div>
<div class="field" style="left:160px;top:654px;width:283px">Age:</div>
<div class="field" style="left:460px;top:654px;width:280px;border-color:var(--blue2);color:var(--blue2);justify-content:space-between">Service:<svg width="10" height="7"><path d="M0 0h10L5 7z" fill="#00a990"/></svg></div>
<div class="field" style="left:757px;top:654px;width:281px">Date:</div>
<div class="btn" style="left:515px;top:737px;width:175px">Book An Appointment</div>

<div class="info-card" style="left:160px"><h4>New Patient offer</h4><p>Lorem Ipsum is simply dummy text of the printing .</p><span class="arrow-dot"><svg width="14" height="12"><path d="M1 6h11M7 1l5 5-5 5" stroke="#fff" stroke-width="1.5" fill="none"/></svg></span></div>
<div class="info-card" style="left:385px"><h4>Accepted Insurance</h4><p>Lorem Ipsum is simply dummy text of the printing .</p><span class="arrow-dot"><svg width="14" height="12"><path d="M1 6h11M7 1l5 5-5 5" stroke="#fff" stroke-width="1.5" fill="none"/></svg></span></div>
<div class="info-card" style="left:610px"><h4>Patient Portal</h4><p>Lorem Ipsum is simply dummy text of the printing .</p><span class="arrow-dot"><svg width="14" height="12"><path d="M1 6h11M7 1l5 5-5 5" stroke="#fff" stroke-width="1.5" fill="none"/></svg></span></div>
<div class="info-card" style="left:835px"><h4>Helpful Tips</h4><p>Lorem Ipsum is simply dummy text of the printing .</p><span class="arrow-dot"><svg width="14" height="12"><path d="M1 6h11M7 1l5 5-5 5" stroke="#fff" stroke-width="1.5" fill="none"/></svg></span></div>

<!-- welcome -->
<div class="rule" style="left:162px;top:1021px"></div>
<h2 class="abs h-title" style="left:162px;top:1028px;line-height:45px">Welcome To<br>The Brightcrest Clinic</h2>
<p class="abs sub" style="left:162px;top:1114px;width:360px">Lorem Ipsum is simply dummy text of the printing and typesetting industry. Lorem Ipsum has been the.</p>
<p class="abs" style="left:162px;top:1178px;width:430px;font-size:10.5px;line-height:19.5px;color:var(--grey)">Welcome to The Brightcrest Clinic where we specialize in General and Cosmetic Dentistry, Dental Implants, Periodontics (Gum Surgery), Endodontics (Root Canal Treatment) and Reconstructive Dentistry for patients in Lakeview, Harborfield, Millbrook, Westgate, Oakridge, Fairhaven, Stonebridge, Elmcourt and all other surrounding neighborhoods of Lakeview, Northshire.</p>
<p class="abs" style="left:162px;top:1296px;width:430px;font-size:10.5px;line-height:19.5px;color:var(--grey)">With Northfield and Eastbrook credentials that inspire confidence, we offer cosmetic dentistry, general dentistry...</p>
<div class="btn" style="left:160px;top:1376px;width:172px">Know More About Us</div>
<div class="abs" style="left:664px;top:1021px;width:262px;height:412px;border:1.5px solid var(--blue2)"></div>
<div class="abs" role="img" aria-label="Portrait of a smiling dentist in a white coat" style="left:712px;top:977px;width:136px;height:493px;border-radius:60px 60px 10px 10px;background:linear-gradient(#eef2f5 0%,#e3e9ee 55%,#5a5f66 62%,#3a3d42 100%)"></div>

<!-- services -->
<div class="svc active" style="left:176px;top:1501px">
  <svg width="48" height="62" viewBox="0 0 48 62"><path d="M10 4c6-3 10 2 14 2s8-5 14-2c7 4 7 16 3 26-2 6-3 14-5 24-1 5-5 5-6 0l-3-14c-1-4-5-4-6 0l-3 14c-1 5-5 5-6 0-2-10-3-18-5-24C3 20 3 8 10 4z" fill="none" stroke="#fff" stroke-width="2.2"/></svg>
  <h4>Cleaning and Prevention</h4><p>Lorem Ipsum is simply dummy text of the printing and typesetting industry.</p>
</div>
<div class="svc" style="left:400px;top:1501px">
  <svg width="62" height="40" viewBox="0 0 62 40"><path d="M4 8c10 8 44 8 54 0M4 8c0 14 10 26 27 26S58 22 58 8" fill="none" stroke="var(--navy)" stroke-width="2.2"/><path d="M12 14v10M20 16v12M28 17v13M36 17v13M44 16v12M52 14v8" stroke="var(--navy)" stroke-width="1.8"/></svg>
  <h4>Cosmetic Dentistry</h4><p>Lorem Ipsum is simply dummy text of the printing and typesetting industry.</p>
</div>
<div class="svc" style="left:147px;top:1710px">
  <svg width="62" height="28" viewBox="0 0 62 28"><path d="M3 6h56c0 10-4 18-28 18S3 16 3 6z" fill="none" stroke="var(--navy)" stroke-width="2.2"/><path d="M13 6v14M23 6v17M33 6v18M43 6v16M51 6v11" stroke="var(--navy)" stroke-width="1.8"/></svg>
  <h4>Implant Dentistry</h4><p>Lorem Ipsum is simply dummy text of the printing and typesetting industry.</p>
</div>
<div class="svc" style="left:370px;top:1710px">
  <h4>Removable Dentures</h4><p>Lorem Ipsum is simply dummy text of the printing and typesetting industry.</p>
</div>
<div class="rule" style="left:642px;top:1602px"></div>
<h2 class="abs h-title" style="left:642px;top:1609px">Our Services</h2>
<p class="abs sub" style="left:642px;top:1656px;width:390px">Lorem Ipsum is simply dummy text of the printing and typesetting industry. Lorem Ipsum has been the industry's standard dummy text ever since the 1500s</p>
<div class="btn" style="left:642px;top:1746px;width:129px">Discover More</div>

<!-- meet us -->
<h2 class="abs h-title center" style="top:1976px">Meet Us</h2>
<p class="abs sub center" style="top:2024px">Lorem Ipsum is simply dummy text of the printing and<br>typesetting industry.</p>
<svg class="abs" style="left:0;top:2090px" width="760" height="380" role="presentation">
  <defs><linearGradient id="meetG" x1="0" y1="0" x2="1" y2="0"><stop offset="0" stop-color="#0592cd"/><stop offset="1" stop-color="#85cae6"/></linearGradient></defs>
  <path d="M0,94 L470,18 Q520,8 545,40 L700,270 Q740,374 640,374 L0,374 Z" fill="url(#meetG)"/>
</svg>
<div class="abs" style="left:162px;top:2220px;width:105px;height:2px;background:#0c2a3c"></div>
<h3 class="abs" style="left:162px;top:2232px;font-family:'Jost',sans-serif;font-weight:500;font-size:18px;color:#fff;letter-spacing:.5px">LENA MORADI, DMD, MS</h3>
<p class="abs" style="left:162px;top:2258px;font-size:11px;font-weight:700;color:#0c2a3c">Board Certified Orthodontist</p>
<p class="abs" style="left:162px;top:2287px;width:430px;font-size:10.5px;line-height:19.5px;color:#eaf6fc">Dr. Lena Moradi graduated summa cum laude with a DMD from Eastbrook University School of Dental Medicine. She was top of her class of 180 Students. She thereafter completed her specialty training in Orthodontics together with a MS degree from Westmoor University.</p>
<div class="abs" style="left:162px;top:2385px;width:36px;height:36px;border-radius:50%;background:rgba(255,255,255,.35);display:flex;align-items:center;justify-content:center"><svg width="14" height="12"><path d="M13 6H2M7 1L2 6l5 5" stroke="#fff" stroke-width="2" fill="none"/></svg></div>
<div class="abs" style="left:212px;top:2385px;width:36px;height:36px;border-radius:50%;background:rgba(255,255,255,.35);display:flex;align-items:center;justify-content:center"><svg width="14" height="12"><path d="M1 6h11M7 1l5 5-5 5" stroke="#fff" stroke-width="2" fill="none"/></svg></div>
<div class="avatar" role="img" aria-label="Team member portrait" style="left:679px;top:2147px;width:62px;height:62px"></div>
<div class="avatar" role="img" aria-label="Team member portrait" style="left:863px;top:2188px;width:38px;height:38px"></div>
<div class="avatar" role="img" aria-label="Portrait of Dr. Lena Moradi" style="left:612px;top:2243px;width:94px;height:94px;border-width:6px"></div>
<div class="avatar" role="img" aria-label="Team member portrait" style="left:760px;top:2265px;width:44px;height:44px"></div>
<div class="avatar" role="img" aria-label="Team member portrait" style="left:927px;top:2293px;width:48px;height:48px"></div>
<div class="avatar" role="img" aria-label="Team member portrait" style="left:803px;top:2368px;width:34px;height:34px"></div>
<div class="avatar" role="img" aria-label="Team member portrait" style="left:886px;top:2366px;width:40px;height:40px"></div>

<!-- blog -->
<h2 class="abs h-title center" style="top:2538px">Our Blog</h2>
<p class="abs sub center" style="top:2587px">Lorem Ipsum is simply dummy text of the printing and<br>typesetting industry.</p>
<div class="abs" style="left:183px;top:2642px;width:270px;height:270px;border-radius:50%;border:7px solid #b7ddef"></div>
<div class="abs" style="left:233px;top:2672px;width:228px;height:228px;border-radius:50%;border:6px solid #b7ddef"></div>
<div class="abs" role="img" aria-label="Photo of a child at a dental checkup" style="left:159px;top:2645px;width:264px;height:264px;border-radius:50%;background:linear-gradient(135deg,#c7d9e4 0%,#e9c7ae 45%,#3aa0d8 75%,#1f84c4 100%)"></div>
<h3 class="abs" style="left:612px;top:2685px;font-family:'Jost',sans-serif;font-weight:500;font-size:19px">Lorem Ipsum is simply dummy text of the.</h3>
<p class="abs" style="left:612px;top:2714px;font-size:10.5px;color:var(--blue)">3-August 2019</p>
<p class="abs" style="left:612px;top:2741px;width:430px;font-size:10.5px;line-height:19.5px;color:var(--grey)">Lorem Ipsum is simply dummy text of the printing and typesetting industry. Lorem Ipsum has been the industry's standard dummy text ever since the 1500s, Lorem Ipsum is simply dummy text of the printing and typesetting industry. Lorem Ipsum has been the industry's standard dummy text ever since the 1500s</p>
<div class="btn" style="left:612px;top:2839px;width:132px">Read More</div>
<div class="abs" style="left:0;top:2983px;width:1200px;height:1px;background:#e6e9eb"></div>

<!-- reviews -->
<div class="rule" style="left:547px;top:3034px"></div>
<h2 class="abs h-title center" style="top:3042px">Clients Review</h2>
<p class="abs sub center" style="top:3090px">Lorem Ipsum is simply dummy text of the printing and<br>typesetting industry.</p>
<div class="review" style="left:160px">Lorem Ipsum is simply dummy text of the printing and typesetting industry. Lorem Ipsum has been the industry's standard dummy text ever since the 1500s, when an unknown printer took a galley of type and scrambled it to make a type specimen book.</div>
<div class="review" style="left:460px">Lorem Ipsum is simply dummy text of the printing and typesetting industry. Lorem Ipsum has been the industry's standard dummy text ever since the 1500s, when an unknown printer took a galley of type and scrambled it to make a type specimen book.</div>
<div class="review" style="left:759px">Lorem Ipsum is simply dummy text of the printing and typesetting industry. Lorem Ipsum has been the industry's standard dummy text ever since the 1500s, when an unknown printer took a galley of type and scrambled it to make a type specimen book.</div>
<div class="review-avatar" role="img" aria-label="Client portrait" style="left:180px"></div><span class="review-name" style="left:250px">-Client Name</span>
<div class="review-avatar" role="img" aria-label="Client portrait" style="left:479px"></div><span class="review-name" style="left:549px">-Client Name</span>
<div class="review-avatar" role="img" aria-label="Client portrait" style="left:778px"></div><span class="review-name" style="left:848px">-Client Name</span>

<!-- contact -->
<h2 class="abs h-title center" style="top:3476px">Contact Us</h2>
<p class="abs sub center" style="top:3524px">Lorem Ipsum is simply dummy text of the printing and<br>typesetting industry.</p>
<div class="field" style="left:160px;top:3605px;width:283px;height:46px">Name:</div>
<div class="field" style="left:460px;top:3605px;width:280px;height:46px">Email:</div>
<div class="field" style="left:757px;top:3605px;width:281px;height:46px">Phone:</div>
<div class="field" style="left:160px;top:3671px;width:878px;height:93px;align-items:flex-start;padding-top:14px">Message:</div>
<div class="btn" style="left:532px;top:3816px;width:132px">Submit Now</div>

<!-- newsletter -->
<div class="abs" style="left:0;top:3921px;width:1200px;height:98px;background:var(--blue)"></div>
<h3 class="abs" style="left:163px;top:3943px;font-family:'Jost',sans-serif;font-weight:500;font-size:27px;color:#fff">Subcribe Now for Our Newsletter</h3>
<p class="abs" style="left:163px;top:3982px;font-size:11px;color:#e3f4fb">Stay current with our news and insight &amp; updates</p>
<div class="abs" style="left:896px;top:3950px;width:142px;height:38px;border:1.5px solid #fff;color:#fff;font-family:'Jost',sans-serif;font-weight:500;font-size:14px;display:flex;align-items:center;justify-content:center">Subscribe Now!</div>

<!-- footer -->
<div class="abs" style="left:160px;top:4058px;display:flex;align-items:center;gap:8px;font-family:'Jost',sans-serif;font-weight:500;font-size:14px;color:var(--blue)"><span class="logo-sq" style="width:24px;height:24px"></span>The Brightcrest Clinic</div>
<p class="abs" style="left:162px;top:4120px;width:210px;font-size:10.5px;line-height:19.5px;color:#555">Lorem Ipsum is simply dummy text of the printing and typesetting industry. Lorem Ipsum has been the industry's standard dummy text ever since .</p>
<span class="social" role="img" aria-label="Social link" style="left:161px"></span>
<span class="social" role="img" aria-label="Social link" style="left:205px"></span>
<span class="social" role="img" aria-label="Social link" style="left:251px;background:var(--blue)"></span>
<span class="social" role="img" aria-label="Social link" style="left:296px"></span>

<h4 class="foot-h" style="left:387px">Quick Links</h4>
<ul class="foot-list" style="left:387px"><li>Home</li><li>About us</li><li>Services</li><li>Meet Us</li><li>Patient Info</li></ul>
<h4 class="foot-h" style="left:613px">Sitemap</h4>
<ul class="foot-list" style="left:613px;line-height:22.5px"><li>Blog</li><li>Client reviews</li><li>Terms &amp; Conditions</li><li>Support</li><li>Appointment</li><li>FAQ</li></ul>
<h4 class="foot-h" style="left:837px">Contact Info</h4>
<svg class="abs" style="left:836px;top:4109px" width="20" height="20"><path d="M5 2l3 4-2 2c1 3 3 5 6 6l2-2 4 3-2 3c-7 0-13-6-13-13z" fill="none" stroke="var(--blue)" stroke-width="1.6"/></svg>
<p class="abs" style="left:875px;top:4112px;font-size:12px">555.014.2288</p>
<svg class="abs" style="left:836px;top:4143px" width="16" height="22"><path d="M8 1a7 7 0 0 1 7 7c0 6-7 13-7 13S1 14 1 8a7 7 0 0 1 7-7z" fill="var(--blue)"/><circle cx="8" cy="8" r="2.6" fill="#fff"/></svg>
<p class="abs" style="left:875px;top:4141px;font-size:11px;line-height:17px;color:#444">120 Harbor Lane, Suite 210,<br>Lakeview NS 02000</p>
<svg class="abs" style="left:836px;top:4203px" width="20" height="14"><rect x="1" y="1" width="18" height="12" fill="var(--blue)"/><path d="M1 1l9 7 9-7" stroke="#fff" stroke-width="1.4" fill="none"/></svg>
<p class="abs" style="left:875px;top:4203px;font-size:11px;color:#444">info@brightcrestclinic-example.com</p>

<div class="abs" style="left:0;top:4298px;width:1200px;height:1px;background:var(--blue2)"></div>
<p class="abs center" style="top:4320px;font-size:10.5px;color:#333">© 2019. <b>The Brightcrest Clinic</b>. All Rights Reserved, Privacy Policy.</p>

</body>
</html>
```